Mental Health

QRT HAVEN
Behavioral Health
4172 W. Pell St. Mesa, AZ 85219
Gwendolyn (480)555-0142 / Omar 480-555-0187

Email: QRTHaven@Mailvex.example
Newly Remodeled & Spacious
g Staff
Registered Nurses
Licensed Independent &
Professional Substance &
Abuse Counselors
Behavioral Health Techs
Certified Caregivers
Behavioral Health &
Substance Abuse Professionals

To Refer a Patient
About Us
QRT Haven is a Fully Staffed Behavioral
Health Residential Facility, providing
treatment plans for adults suffering
with various Behavioral Health and
Substance Abuse disorders, while living
in a nice safe, clean and supportive
environment. Our home offers clients the
ability to learn the necessary skills to
help clients adapt, build self confidence
as well as independence, with the goal
of reducing the probability of a future
crisis or possible relapse. We offer
counseling programs, consisting of a
variety of addiction and recovery support
groups, independent living, coping and
social skills groups, as well as assisting
clients with using tools to create a resume
to help obtain employment and so much
more. We are committed to teaching
self management care and allowing
clients to understand how to utilize the
resources, skills and tools available for
long term success by providing superior
quality, all-inclusive living arrangements
and treatment options.

Thank you for your patience while I update the final content needed for us to make the final decision this week.

```html
<!DOCTYPE html>
<html lang="en">
<head>
<meta charset="utf-8">
<title>QRT Haven – Business Card</title>
<link href="https://fonts.googleapis.com/css2?family=Montserrat:wght@400;500&display=swap" rel="stylesheet">
<style>
  :root{
    --bg:#2b2b2d;
    --card:#ffffff;
    --blue:#0a6cb8;
    --green:#7db441;
    --white:#ffffff;
  }
  html,body{margin:0;padding:0;overflow:hidden;}
  body{width:1200px;height:880px;background:var(--bg);position:relative;font-family:'Montserrat',sans-serif;}
  .card{position:absolute;width:580px;height:330px;background:var(--card);border-radius:22px;overflow:hidden;box-shadow:0 14px 30px rgba(0,0,0,.45);}
  .card--front{left:70px;top:70px;}
  .card--back{left:550px;top:480px;}
  .wordmark{position:absolute;display:flex;align-items:center;gap:16px;}
  .card--front .wordmark{left:50%;top:50%;transform:translate(-50%,-50%);}
  .card--back .wordmark{left:44px;top:118px;gap:14px;}
  .wordmark__dot{width:58px;height:58px;border-radius:50%;background:var(--blue);flex:none;}
  .card--back .wordmark__dot{width:50px;height:50px;}
  .wordmark__name{font-weight:500;font-size:40px;letter-spacing:2px;color:var(--blue);white-space:nowrap;}
  .card--back .wordmark__name{font-size:33px;}
  .card__waves{position:absolute;inset:0;width:580px;height:330px;}
  .holder{position:absolute;right:34px;top:24px;text-align:right;}
  .holder__name{font-size:22px;color:var(--blue);font-weight:500;line-height:1;}
  .holder__role{font-size:14px;color:var(--green);margin-top:3px;}
  .contact{position:absolute;right:28px;top:150px;text-align:right;color:var(--white);font-size:12px;line-height:1.55;}
  .contact__address{margin-bottom:12px;}
  .contact__line{display:flex;justify-content:flex-end;align-items:center;gap:7px;white-space:nowrap;}
  .contact__icon{width:15px;height:15px;flex:none;}
</style>
</head>
<body>
  <section class="card card--front">
    <div class="wordmark">
      <span class="wordmark__dot"></span>
      <span class="wordmark__name">QRT HAVEN</span>
    </div>
  </section>

  <section class="card card--back">
    <svg class="card__waves" viewBox="0 0 580 330" aria-hidden="true">
      <path d="M580,88 C470,95 400,130 360,185 C320,245 280,300 150,315 L0,318 L0,330 L580,330 Z" fill="var(--blue)"/>
      <path d="M555,82 C455,92 385,127 343,182 C303,242 262,297 120,312" fill="none" stroke="var(--blue)" stroke-width="4"/>
      <path d="M300,165 C285,255 200,295 0,300 L0,312 C220,308 300,265 300,165 Z" fill="var(--green)"/>
    </svg>

    <div class="wordmark">
      <span class="wordmark__dot"></span>
      <span class="wordmark__name">QRT HAVEN</span>
    </div>

    <div class="holder">
      <div class="holder__name">Gwendolyn</div>
      <div class="holder__role">Owner</div>
    </div>

    <div class="contact">
      <div class="contact__address">4172 W. Pell St.<br>Mesa, AZ 85219</div>
      <div class="contact__line">(480)555-0142
        <svg class="contact__icon" viewBox="0 0 16 16" aria-hidden="true"><circle cx="8" cy="8" r="8" fill="var(--green)"/><path d="M5.2,4 L6.6,4 L7.2,6 L6.3,6.8 C6.8,7.9 7.7,8.8 8.9,9.4 L9.7,8.5 L11.7,9.1 L11.7,10.6 C8,11 4.8,7.8 5.2,4 Z" fill="#fff"/></svg>
      </div>
      <div class="contact__line">QRTHaven@Mailvex.example
        <svg class="contact__icon" viewBox="0 0 16 16" aria-hidden="true"><circle cx="8" cy="8" r="8" fill="var(--green)"/><rect x="4" y="5" width="8" height="6" fill="#fff"/><path d="M4,5 L8,8.3 L12,5" fill="none" stroke="var(--green)" stroke-width="1"/></svg>
      </div>
    </div>
  </section>
</body>
</html>
```